Offer banner redesign / Simplifying existing banner

We have a banner there customer can click on to get an offer. We want to simplify this banner and to get it to at minimum. We are not clear about how it shoulderstand look like, but the actual banner you can see here (It's at the top of the page): https://kaminwerk-vorhof.de/rauchrohr-stahl/ We want to get rid of the icons and to reduce the size of the baner. The baner shoulderstand contain the Following text: Affordable chimney using installation service button text: Request free quote

Target Market(s)

Customers from age of 40yrs.

Requirements
Must have
• Clear and good visible button
Nice to have
• It Should be simple and striking.

```html
<!DOCTYPE html>
<html lang="de">
<head>
<meta charset="utf-8">
<title>Kaminwerk Vorhof – Rauchrohr Stahl</title>
<link href="https://fonts.googleapis.com/css2?family=Signika:wght@300;400;600;700&family=Open+Sans:wght@400;600&display=swap" rel="stylesheet">
<style>
  :root{
    --stage:#ececec;
    --white:#ffffff;
    --bar:#e8e8e8;
    --side:#f0f0f0;
    --line:#dddddd;
    --ink:#222222;
    --muted:#555555;
    --orange:#f5a623;
    --orange-deep:#e57e00;
    --orange-light:#ffa31a;
    --star:#f7c600;
    --green:#2db52d;
    --select:#a9a9a9;
  }
  *{box-sizing:border-box;margin:0;padding:0}
  html,body{width:1200px;height:1200px;overflow:hidden}
  body{background:var(--stage);font-family:"Signika",sans-serif;color:var(--ink);position:relative}
  .page{position:absolute;left:0;top:346px;width:1200px;height:508px;background:var(--white);overflow:hidden;box-shadow:0 2px 6px rgba(0,0,0,.25)}
  .abs{position:absolute}

  .topbar{left:0;top:0;width:1200px;height:32px;background:var(--bar)}
  .topbar__link{top:10px;font-family:"Open Sans",sans-serif;font-size:10px;letter-spacing:1px;color:#333}
  .topbar__sep{top:8px;width:1px;height:18px;background:#777}
  .topbar__rating{left:776px;top:8px;font-size:11px;color:#333}
  .topbar__rating .stars{color:var(--star);letter-spacing:-1px;font-size:13px}
  .topbar__box{top:4px;height:28px;background:#dcdcdc;font-size:10px;color:#444;padding:8px 8px;display:flex;gap:10px;align-items:flex-start}

  .header{left:0;top:32px;width:1200px;height:64px;border-bottom:1px solid var(--line)}
  .brand{left:46px;top:14px;display:flex;align-items:center;gap:10px}
  .brand__dot{width:40px;height:40px;border-radius:50%;background:var(--orange)}
  .brand__name{font-size:22px;font-weight:600;color:#333;line-height:1}
  .search{left:426px;top:10px;width:348px;height:40px;border:2px solid #ddd;border-radius:10px;overflow:hidden}
  .search__text{left:52px;top:10px;font-size:14px;font-weight:300;color:#999}
  .search__btn{right:0;top:0;width:44px;height:36px;background:var(--orange)}
  .phone{left:956px;top:14px}
  .phone__num{left:32px;top:0;font-size:20px;font-weight:600;color:var(--orange);white-space:nowrap;letter-spacing:.5px}
  .phone__hours{left:26px;top:28px;font-size:10px;color:#444;white-space:nowrap}

  .nav{left:0;top:96px;width:1200px;height:44px;border-bottom:1px solid var(--line)}
  .nav__item{top:12px;font-size:15px;font-weight:600;color:#222}
  .nav__chev{color:#888;font-weight:300;margin-left:12px;font-size:12px}
  .nav__sep{left:190px;top:16px;width:1px;height:16px;background:#bbb}
  .badge{left:951px;top:6px;width:34px;height:34px;border-radius:50%;background:#333;border:3px solid var(--star)}
  .review__label{left:1000px;top:8px;font-size:10px;font-weight:300;color:#888}
  .review__stars{left:1008px;top:20px;color:var(--star);font-size:15px;letter-spacing:-1px}
  .review__grade{left:1097px;top:8px;font-size:11px;font-weight:600;color:#222}
  .review__score{left:1090px;top:22px;font-size:15px;color:#222}
  .review__score b{font-weight:600}

  .offer{left:0;top:140px;width:1200px;height:149px;background:var(--side)}
  .offer__panel{left:145px;top:0;width:927px;height:149px;background:var(--white)}
  .offer__title{left:270px;top:50px;font-size:45px;font-weight:700;color:var(--orange);white-space:nowrap;letter-spacing:-.3px}
  .offer__btn{left:770px;top:46px;width:283px;height:62px;border-radius:31px;background:linear-gradient(#ff9d0a,#e97a00);box-shadow:0 2px 0 #c96600,0 3px 6px rgba(0,0,0,.35);border:2px solid #ffc266}
  .offer__btn-text{left:44px;top:10px;width:180px;text-align:center;font-size:16px;line-height:21px;color:#fff;letter-spacing:-.8px;font-weight:400}
  .offer__btn-icon{left:236px;top:14px;width:30px;height:30px;border-radius:50%;background:#f4b54a;border:2px solid #ffd089}

  .content-side{left:1180px;top:289px;width:20px;height:219px;background:var(--side)}
  .crumbs{left:59px;top:299px;font-size:12px;font-weight:300;color:var(--orange-deep)}
  .crumbs__gt{color:#666;margin:0 12px}
  .category{left:333px;top:334px;font-size:24px;font-weight:400;color:#222;letter-spacing:.3px}
  .pager{left:341px;top:377px;display:flex;gap:18px;align-items:center;font-size:12px;color:#555}
  .pager__current{width:22px;height:22px;border-radius:50%;background:#999;color:#fff;display:flex;align-items:center;justify-content:center;margin-right:-4px}
  .show{left:1011px;top:379px;font-size:14px;font-weight:600;color:#555}
  .show__select{left:1056px;top:377px;width:58px;height:28px;background:var(--select);color:#fff;font-size:13px;padding:5px 0 0 9px}
  .rule{left:333px;top:409px;width:790px;height:2px;background:#e6e6e6}
  .filter{left:60px;top:418px;width:244px;height:43px;background:var(--orange);color:#fff;font-size:15px;font-weight:300;padding:12px 0 0 14px}
  .chat{left:20px;top:450px;width:133px;height:44px;background:var(--green);border-radius:4px 4px 0 0;color:#fff;font-size:13px;font-weight:600;padding:13px 0 0 56px}
  .card{top:434px;width:380px;height:80px;border:2px solid #eee;text-align:center;font-size:14px;line-height:22px;color:#222;padding-top:14px}
</style>
</head>
<body>
<main class="page">
  <div class="abs topbar">
    <span class="abs topbar__link" style="left:80px">SICHER EINKAUFEN ▾</span>
    <span class="abs topbar__sep" style="left:224px"></span>
    <span class="abs topbar__link" style="left:237px">VORTEILE ▾</span>
    <span class="abs topbar__sep" style="left:328px"></span>
    <span class="abs topbar__link" style="left:342px">BERATUNG &amp; KONTAKT ▾</span>
    <span class="abs topbar__rating"><span class="stars">★★★★★</span> (4.55/5.00) ✓</span>
    <div class="abs topbar__box" style="left:927px;width:98px">Mein Konto
      <svg width="16" height="16" viewBox="0 0 16 16"><circle cx="8" cy="5" r="4" fill="#222"/><path d="M1 16c0-5 3-7 7-7s7 2 7 7z" fill="#222"/></svg></div>
    <div class="abs topbar__box" style="left:1038px;width:89px">Warenkorb
      <svg width="18" height="18" viewBox="0 0 18 18"><circle cx="12" cy="4" r="4" fill="var(--orange)"/><path d="M2 8h14l-2 9H4z" fill="#444"/></svg></div>
  </div>

  <header class="abs header">
    <div class="abs brand"><span class="brand__dot"></span><span class="brand__name">Kaminwerk Vorhof</span></div>
    <div class="abs search">
      <span class="abs search__text">Suchbegriff oder Artikelnummer</span>
      <span class="abs search__btn">
        <svg width="44" height="36" viewBox="0 0 44 36"><circle cx="21" cy="17" r="6" fill="none" stroke="#fff" stroke-width="2.5"/><line x1="25" y1="21" x2="29" y2="25" stroke="#fff" stroke-width="2.5"/></svg>
      </span>
    </div>
    <div class="abs phone">
      <svg class="abs" style="left:0;top:2px" width="22" height="22" viewBox="0 0 22 22"><path d="M4 3l4 1 1 5-2 2c1 3 3 5 5 6l2-2 5 1 1 4c-9 1-17-7-16-17z" fill="var(--orange)"/></svg>
      <span class="abs phone__num">0421 / 338 190 0</span>
      <span class="abs phone__hours">Mo. - Fr. von 09:00 bis 18:00 Uhr</span>
    </div>
  </header>

  <nav class="abs nav">
    <span class="abs nav__item" style="left:61px">Online-Shop<span class="nav__chev">﹀</span></span>
    <span class="abs nav__sep"></span>
    <span class="abs nav__item" style="left:209px">Service<span class="nav__chev">﹀</span></span>
    <span class="abs badge"></span>
    <span class="abs review__label">Kundenbewertung</span>
    <span class="abs review__stars">★★★★★</span>
    <span class="abs review__grade">sehr gut</span>
    <span class="abs review__score"><b>4.55</b>/5.00</span>
  </nav>

  <section class="abs offer">
    <div class="abs offer__panel"></div>
    <h2 class="abs offer__title">Preiswerter Schornstein</h2>
    <a class="abs offer__btn">
      <span class="abs offer__btn-text">KOSTENLOSES ANGEBOT ANFORDERN</span>
      <span class="abs offer__btn-icon">
        <svg width="26" height="26" viewBox="0 0 26 26"><path d="M13 7v10M9 13l4 4 4-4" fill="none" stroke="#8a4a00" stroke-width="2"/></svg>
      </span>
    </a>
  </section>

  <div class="abs content-side"></div>
  <div class="abs crumbs">Kaminwerk-Vorhof<span class="crumbs__gt">&gt;</span>Edelstahlschornstein</div>
  <h1 class="abs category">Edelstahlschornstein</h1>
  <div class="abs pager"><span class="pager__current">1</span><span>2</span><span>3</span><span>4</span><span>5</span></div>
  <span class="abs show">Zeige</span>
  <div class="abs show__select">12 <span style="margin-left:12px">﹀</span></div>
  <div class="abs rule"></div>

  <div class="abs card" style="left:333px">Edelstahlschornstein doppelwandig Ø 150 mm<br>Bausatz - Varenholt DW-ECO</div>
  <div class="abs card" style="left:743px">Edelstahlschornstein doppelwandig Ø 150 mm<br>Bausatz - Varenholt DW-FU</div>

  <div class="abs filter">Filter
    <svg class="abs" style="right:14px;top:17px" width="12" height="12" viewBox="0 0 12 12"><path d="M0 0h12L7 6v6L5 10V6z" fill="#fff"/></svg>
  </div>
  <div class="abs chat">
    <svg class="abs" style="left:18px;top:11px" width="30" height="22" viewBox="0 0 30 22"><path d="M2 0h26v16H10l-6 6v-6H2z" fill="#fff"/><circle cx="9" cy="8" r="2" fill="var(--green)"/><circle cx="15" cy="8" r="2" fill="var(--green)"/><circle cx="21" cy="8" r="2" fill="var(--green)"/></svg>
    Live-Chat
  </div>
</main>
</body>
</html>
```